Gourmet Food Items, Modern

In need of an updated label for our Gourmet Food Line, which includes Mustards, Preserves and Pickled Foods. We have very specific requirements to meet from the label manufacturer (requirements are in the uploaded files). 2 sizes are needed, 2.5"x5.75" and 1.5"x5.75", each has their own specific criteria to meet. Aside from the label manufacturer requirements, we ask that the label is easy to read and well branded, unique and not dark. We prefer a modern, sleek look, but remain open to a fun and whimsical design.
Updates

Reason: Only received 3 designs

Target Market(s)

18-65 years old, with majority of clients 30-45 year old female.

Font styles to use
Sans Serif

Requirements
Must have
• Space for Ingredients, Nutrition Facts and Barcode. Neutral for a broad range of food items.
Should not have
• Can not be DARK! We have poor lighting in our store and dark labels are lost in shelving shadows.

```html
<!DOCTYPE html>
<html lang="en">
<head>
<meta charset="utf-8">
<title>Gourmet Food Line – Mustard Label, Format C</title>
<link rel="stylesheet" href="https://fonts.googleapis.com/css2?family=Cinzel:wght@400;600&family=Dancing+Script:wght@500&family=Roboto:ital,wght@0,700;1,900&family=Roboto+Condensed:wght@400&display=swap">
<style>
  :root {
    --sheet: #ffffff;
    --sheet-edge: #9a9a9a;
    --label-gold: #f2b316;
    --label-gold-deep: #e3a40c;
    --label-pale: #fdf0c2;
    --label-cream: #fff9e6;
    --ink: #1e1e1e;
    --ink-soft: #3a3a3a;
    --accent-red: #d9233a;
    --leaf: #a9b43a;
    --guide: #6a6a6a;
  }
  html, body {
    margin: 0;
    padding: 0;
    width: 1200px;
    height: 849px;
    overflow: hidden;
    background: var(--sheet);
  }
  .sheet {
    position: relative;
    width: 1198px;
    height: 847px;
    border: 1px solid var(--sheet-edge);
  }
  .sheet-art {
    position: absolute;
    inset: 0;
  }
  .format-heading {
    position: absolute;
    left: 700px;
    top: 100px;
    width: 480px;
    text-align: center;
    color: var(--ink);
  }
  .format-heading__title {
    margin: 0;
    font: italic 900 25px/1 "Roboto", sans-serif;
  }
  .format-heading__kicker {
    margin: 9px 0 0;
    font: 400 15px/1 "Roboto Condensed", sans-serif;
  }
  .format-heading__letter {
    margin: 2px 0 0;
    font: 700 54px/1 "Roboto", sans-serif;
  }
  .spec-text { font-family: "Roboto Condensed", sans-serif; fill: var(--ink); }
  .dim-box-text { font-family: "Roboto", sans-serif; font-weight: 700; fill: var(--ink); }
  .label-serif { font-family: "Cinzel", serif; }
  .label-script { font-family: "Dancing Script", cursive; }
  .label-brand { font-family: "Roboto", sans-serif; font-weight: 700; }
</style>
</head>
<body>
<main class="sheet">
  <svg class="sheet-art" width="1198" height="847" viewBox="0 0 1198 847" xmlns="http://www.w3.org/2000/svg">
    <defs>
      <linearGradient id="label-ground" x1="0" y1="0" x2="0" y2="1">
        <stop offset="0" stop-color="var(--label-pale)"/>
        <stop offset="0.5" stop-color="var(--label-cream)"/>
        <stop offset="1" stop-color="var(--label-pale)"/>
      </linearGradient>
      <linearGradient id="flower-tone" x1="0" y1="0" x2="0" y2="1">
        <stop offset="0" stop-color="#f5dc3a"/>
        <stop offset="1" stop-color="var(--leaf)"/>
      </linearGradient>
      <marker id="arrow-head" viewBox="0 0 10 10" refX="9" refY="5" markerWidth="9" markerHeight="9" orient="auto-start-reverse">
        <path d="M0,1 L10,5 L0,9 Z" fill="var(--ink)"/>
      </marker>
      <path id="crest-arc" d="M72,52 Q155,8 238,52"/>

      <symbol id="mustard-label" viewBox="0 0 588 258">
        <rect x="0.5" y="0.5" width="587" height="257" rx="9" fill="url(#label-ground)" stroke="#8a8a8a" role="img" aria-label="Pale yellow scallop wave pattern"/>
        <rect class="label-band" x="0" y="58" width="588" height="125" fill="var(--label-gold)"/>
        <rect class="label-band-inset" x="10" y="64" width="572" height="112" fill="none" stroke="#ffffff" stroke-width="2"/>

        <path class="crest-frame" d="M35,42 Q155,-6 275,42 L268,192 Q155,276 42,192 Z" fill="var(--label-gold)" stroke="var(--ink-soft)" stroke-width="3"/>
        <path class="crest-panel" d="M50,62 Q155,38 260,62 L254,188 Q155,258 56,188 Z" fill="#ffffff" stroke="var(--label-gold-deep)" stroke-width="2"/>
        <text class="label-serif" font-size="15" fill="var(--ink-soft)" letter-spacing="1">
          <textPath href="#crest-arc" startOffset="50%" text-anchor="middle">·GOURMET FOOD LINE·</textPath>
        </text>

        <text class="label-brand" x="158" y="100" font-size="22" fill="var(--ink)" text-anchor="middle">THE PANTRY LOFT</text>

        <rect class="crest-flower" x="46" y="118" width="44" height="106" rx="18" fill="url(#flower-tone)" opacity="0.85" role="img" aria-label="Illustration of a yellow mustard flower sprig"/>

        <text class="label-serif" x="162" y="158" font-size="24" fill="var(--ink-soft)" text-anchor="middle">MUSTARD</text>
        <text class="label-script" x="160" y="181" font-size="19" fill="var(--accent-red)" text-anchor="middle">Classic Yellow</text>

        <path class="quality-ribbon" d="M112,210 H198 V220 L155,225 L112,220 Z" fill="var(--ink-soft)"/>
        <text class="label-serif" x="155" y="218" font-size="6" fill="#ffffff" text-anchor="middle" font-weight="600">QUALITY PRODUCTS</text>
      </symbol>
    </defs>

    <line class="heading-rule" x1="636" y1="88" x2="1192" y2="88" stroke="#cfcfcf"/>

    <!-- finished label -->
    <use href="#mustard-label" x="94" y="106" width="588" height="258"/>

    <!-- width dimension -->
    <line x1="110" y1="420" x2="680" y2="420" stroke="var(--ink)" stroke-width="1.5" marker-start="url(#arrow-head)" marker-end="url(#arrow-head)"/>
    <rect x="365" y="405" width="58" height="29" fill="#ffffff" stroke="var(--ink)" stroke-width="1.5"/>
    <text class="dim-box-text" x="394" y="427" font-size="18" text-anchor="middle">5.75"</text>

    <!-- height dimension -->
    <line x1="50" y1="479" x2="50" y2="731" stroke="var(--ink)" stroke-width="1.5" marker-start="url(#arrow-head)" marker-end="url(#arrow-head)"/>
    <line x1="28" y1="478" x2="72" y2="478" stroke="var(--ink)"/>
    <line x1="28" y1="732" x2="72" y2="732" stroke="var(--ink)"/>
    <rect x="23" y="585" width="54" height="27" fill="#ffffff" stroke="var(--ink)" stroke-width="1.5"/>
    <text class="dim-box-text" x="50" y="605" font-size="17" text-anchor="middle">2.5"</text>

    <!-- guide lines -->
    <g stroke="var(--guide)" stroke-dasharray="6 5" fill="none">
      <line x1="690" y1="400" x2="690" y2="805"/>
      <line x1="104" y1="440" x2="104" y2="775"/>
    </g>
    <g stroke="var(--guide)">
      <line x1="700" y1="483" x2="712" y2="483"/>
      <line x1="696" y1="727" x2="712" y2="727"/>
      <line x1="696" y1="732" x2="712" y2="732"/>
      <line x1="720" y1="741" x2="768" y2="741"/>
    </g>
    <text class="spec-text" x="728" y="506" font-size="11">1/16"</text>
    <text class="spec-text" x="728" y="697" font-size="11">1/16</text>

    <!-- template label -->
    <use href="#mustard-label" x="104" y="478" width="586" height="254"/>
    <text class="spec-text" x="216" y="467" font-size="14" text-anchor="middle">Centered 1.5"</text>

    <g class="template-zones" transform="translate(104 478)">
      <g fill="none" stroke="var(--guide)" stroke-dasharray="4 3">
        <ellipse cx="152" cy="58" rx="140" ry="52"/>
        <rect x="12" y="138" width="282" height="108" rx="12"/>
        <rect x="306" y="5" width="102" height="153" rx="12"/>
        <rect x="420" y="5" width="160" height="165" rx="12"/>
        <rect x="306" y="172" width="102" height="74" rx="12"/>
        <rect x="420" y="182" width="162" height="64" rx="12"/>
      </g>

      <line x1="252" y1="4" x2="252" y2="126" stroke="var(--ink)" marker-start="url(#arrow-head)" marker-end="url(#arrow-head)"/>
      <text class="spec-text" font-size="12" transform="translate(264 56) rotate(-90)" text-anchor="middle">1.25</text>
      <text class="spec-text" font-size="10" transform="translate(10 52) rotate(-90)" text-anchor="middle">1/8</text>
      <text class="spec-text" font-size="10" transform="translate(304 52) rotate(-90)" text-anchor="middle">1/8</text>

      <text class="spec-text" x="156" y="76" font-size="12" text-anchor="middle">LOGO WIDTH - 2.75"</text>
      <text class="spec-text" x="152" y="202" font-size="13" text-anchor="middle">Product &amp; Weight</text>

      <text class="spec-text" font-size="15" text-anchor="middle">
        <tspan x="356" y="70">Ingredients</tspan>
        <tspan x="356" y="86">&amp; V.O.</tspan>
        <tspan x="356" y="102">Qualifier</tspan>
      </text>
      <text class="spec-text" x="501" y="80" font-size="15" text-anchor="middle">Nutrition Facts</text>

      <line x1="322" y1="172" x2="322" y2="246" stroke="var(--ink)" marker-start="url(#arrow-head)" marker-end="url(#arrow-head)"/>
      <text class="spec-text" x="327" y="214" font-size="13">.75"</text>
      <text class="spec-text" font-size="15" text-anchor="middle">
        <tspan x="372" y="200">Address</tspan>
        <tspan x="372" y="220">Info</tspan>
      </text>
      <text class="spec-text" x="501" y="219" font-size="15" text-anchor="middle">UPC#</text>
    </g>

    <!-- 1 inch dimension -->
    <line x1="410" y1="734" x2="410" y2="750" stroke="var(--ink)"/>
    <line x1="510" y1="734" x2="510" y2="750" stroke="var(--ink)"/>
    <line x1="412" y1="742" x2="448" y2="742" stroke="var(--ink)" marker-start="url(#arrow-head)"/>
    <line x1="472" y1="742" x2="508" y2="742" stroke="var(--ink)" marker-end="url(#arrow-head)"/>
    <text class="spec-text" x="460" y="747" font-size="14" text-anchor="middle">1"</text>
  </svg>

  <header class="format-heading">
    <h1 class="format-heading__title">Medium Foil Ctr w/Nutrition Info (FN)</h1>
    <p class="format-heading__kicker">FORMAT</p>
    <p class="format-heading__letter">C</p>
  </header>
</main>
</body>
</html>
```